Cardiology Practice needs a Heart Scan Order Form

Busy cardiology practice needs an order form for a heart scan test. Sample is attached. One side should have all information noted and the other side should have our physician names (Vikram Joshi, MD, K.L. Morvandi, MD, Anjali Desai, MD, Parvin Joshi, MD, and Gerald Montefino, MD. It should have the map that is uploaded and our demographic information (Crestline Cardio PLLC, 218 Juniper Ave. Ste. B, Webster, TX 77412 along with phone 713-642-1187 and fax 713-642-1188) as well as our web address (crestlinecardio.example). Our primary colors are red, black and white. Needs to fit paper size 8 1/2 by 11.

Target Market(s)

Healthcare

Industry/Entity Type

Health Care

Font styles to use
Serif

Colors
ec1f27

Requirements
Must have
• Logo, information listed on sample form, demographics and physician names as well as website.
Nice to have
• Open to suggestions
Should not have
• Physician Pictures

```html
<!DOCTYPE html>
<html lang="en">
<head>
<meta charset="utf-8">
<title>Crestline Cardio – Calcium Score Heart Scan Order Form</title>
<link rel="stylesheet" href="https://fonts.googleapis.com/css2?family=Montserrat:wght@400;600;700;800&family=Roboto:ital,wght@0,400;0,500;1,700&family=Roboto+Condensed:ital,wght@0,400;0,700;1,700&display=swap">
<style>
:root{
  --red:#c1272d;
  --black:#2b2b2b;
  --ink:#222;
  --grey-text:#4a4a4a;
  --panel:#e4e4e4;
  --stage:#6f6f6f;
  --map:#e8e6e1;
  --white:#fff;
}
*{box-sizing:border-box;margin:0;padding:0}
html,body{width:1200px;height:893px;overflow:hidden}
body{background:var(--stage);position:relative;font-family:'Roboto',Arial,sans-serif;color:var(--ink)}
.sheet{position:absolute;top:81px;width:505px;height:715px;background:var(--white);box-shadow:0 10px 24px rgba(0,0,0,.35);overflow:hidden}
.sheet--front{left:74px}
.sheet--form{left:626px}

/* front */
.front-art{position:absolute;inset:0}
.brand{position:absolute;left:0;right:0;top:78px;text-align:center;font-family:'Montserrat',sans-serif;font-weight:800;color:var(--red);font-size:38px;letter-spacing:1px;line-height:1;white-space:nowrap}
.brand-mark{display:inline-block;width:22px;height:22px;border-radius:50%;background:var(--red);margin-right:12px;vertical-align:2px}
.physicians{position:absolute;left:0;right:0;top:177px;text-align:center;font-family:'Montserrat',sans-serif;font-weight:700;color:var(--red);font-size:19.5px;line-height:23.5px;text-transform:uppercase}
.practice-address{position:absolute;left:0;right:0;top:602px;text-align:center;font-family:'Montserrat',sans-serif;font-size:14.2px;line-height:18.3px;color:var(--grey-text);text-transform:uppercase}
.web-pill{position:absolute;left:50%;transform:translateX(-50%);top:667px;height:23px;padding:0 14px;border-radius:12px;background:var(--red);color:var(--white);font-family:'Montserrat',sans-serif;font-weight:700;font-size:14px;line-height:23px;text-align:center;text-transform:uppercase;letter-spacing:.4px;white-space:nowrap}

/* form */
.form-title{position:absolute;left:27px;top:21px;width:452px;height:40px;background:var(--red);color:var(--white);font-family:'Montserrat',sans-serif;font-weight:700;font-size:23px;letter-spacing:2.6px;line-height:40px;text-align:center}
.form-brand{position:absolute;left:60px;top:106px;font-family:'Montserrat',sans-serif;font-weight:800;color:var(--red);font-size:13.5px;line-height:1;white-space:nowrap}
.form-brand .brand-mark{width:11px;height:11px;margin-right:6px;vertical-align:0}
.schedule{position:absolute;left:258px;top:92px;font-family:'Montserrat',sans-serif;font-size:10.5px;line-height:15.5px;color:var(--grey-text);font-weight:600}
.schedule h3{color:var(--red);font-size:12px;font-weight:700;margin-bottom:1px}
.schedule .dots{display:inline-block;width:136px;border-bottom:1px dotted #777;margin-left:2px}

.form-panel{position:absolute;left:23px;top:153px;width:459px;height:270px;background:var(--panel)}
.section-bar{position:absolute;left:27px;width:452px;height:19px;background:var(--red);color:var(--white);font-weight:500;font-size:10.5px;line-height:19px;text-align:center;text-transform:uppercase}
.field-row{position:absolute;left:26px;width:454px;display:flex;align-items:flex-end;font-size:10.4px;white-space:nowrap;line-height:12px}
.fill{flex:1;border-bottom:1px dotted #555;margin:0 3px 2px 2px}
.fill--fixed{flex:none}
.check-row{position:absolute;left:27px;width:452px;display:flex;justify-content:space-between;font-size:10.4px;line-height:12px;white-space:nowrap}
.box{display:inline-block;width:8px;height:8px;border:1px solid var(--red);margin-right:4px;vertical-align:-1px;background:var(--white)}
.box-dots{display:inline-block;border-bottom:1px dotted #555;margin:0 1px}

.notice{position:absolute;left:26px;top:426px;font-family:'Roboto Condensed',sans-serif;font-style:italic;font-weight:700;font-size:7.8px}
.instructions{position:absolute;left:27px;top:441px;width:400px;list-style:none;font-family:'Roboto Condensed',sans-serif;font-size:7.6px;line-height:10.2px}
.instructions li{position:relative;padding-left:12px}
.instructions li::before{content:"";position:absolute;left:0;top:2px;width:6px;height:6px;border:1px solid var(--red)}
.instructions u{text-decoration:underline}
.acknowledge{position:absolute;left:26px;top:555px;width:455px;font-family:'Roboto Condensed',sans-serif;font-size:7.7px;line-height:10.4px}

.sign-line{position:absolute;width:146px;border-top:1.5px solid var(--red);padding-top:2px;font-style:italic;font-weight:700;font-size:10px}
.referrer{position:absolute;left:340px;top:579px;width:139px;border:1px solid var(--red);font-family:'Roboto Condensed',sans-serif;font-size:7.8px}
.referrer h4{background:var(--red);color:var(--white);font-weight:400;font-size:7.8px;padding:2px 6px;line-height:9px}
.referrer div{background:var(--panel);padding:0 6px;height:18px;line-height:18px;border-top:1px solid #fff}
.form-footer{position:absolute;left:0;right:0;top:672px;text-align:center;font-size:9.6px;line-height:12.8px}
</style>
</head>
<body>

<section class="sheet sheet--front">
  <svg class="front-art" width="505" height="715" viewBox="0 0 505 715">
    <rect x="0" y="210" width="505" height="430" fill="var(--map)" role="img" aria-label="Street map showing the Crestline Cardio office location in Webster, Texas"/>
    <path d="M0,0 H505 V222 C400,292 150,300 0,238 Z" fill="var(--white)"/>
    <path d="M0,238 C150,300 400,292 505,222 V236 C400,306 150,312 0,268 Z" fill="var(--black)"/>
    <path d="M0,238 C150,300 400,292 505,222 V250 C400,304 150,306 0,246 Z" fill="var(--red)"/>
    <path d="M0,640 C130,592 300,560 505,580 V715 H0 Z" fill="var(--white)"/>
    <path d="M0,612 C130,560 300,532 505,558 V580 C300,560 130,592 0,640 Z" fill="var(--black)"/>
    <path d="M0,612 C130,560 300,532 505,558 V568 C300,552 130,584 0,640 Z" fill="var(--red)"/>
  </svg>
  <div class="brand"><span class="brand-mark"></span>CRESTLINE CARDIO</div>
  <div class="physicians">
    Vikram Joshi, MD | K.L. Morvandi, MD<br>
    Anjali Desai, MD | Parvin Joshi, MD<br>
    Gerald Montefino, MD
  </div>
  <div class="practice-address">
    Crestline Cardio PLLC<br>
    218 Juniper Ave. Ste. B, Webster, TX 77412<br>
    Phone 713-642-1187 &amp; Fax 713-642-1188
  </div>
  <div class="web-pill">crestlinecardio.example</div>
</section>

<section class="sheet sheet--form">
  <h1 class="form-title">CALCIUM SCORE HEART SCAN</h1>
  <div class="form-brand"><span class="brand-mark"></span>CRESTLINE CARDIO</div>
  <div class="schedule">
    <h3>TEST SCHEDULE</h3>
    Test date:<span class="dots"></span><br>
    Test time:<span class="dots"></span>
  </div>

  <div class="form-panel"></div>
  <div class="section-bar" style="top:156px">Patient Information</div>
  <div class="field-row" style="top:182px">Name:<span class="fill"></span>Mi:<span class="fill fill--fixed" style="width:236px"></span></div>
  <div class="field-row" style="top:202px">Date of birth:<span class="fill"></span>Account no:<span class="fill fill--fixed" style="width:230px"></span></div>

  <div class="section-bar" style="top:225px">Contact Information</div>
  <div class="field-row" style="top:252px">Address:<span class="fill"></span></div>
  <div class="field-row" style="top:272px">Home phone no:<span class="fill fill--fixed" style="width:138px"></span>Mobile phone no:<span class="fill"></span></div>

  <div class="section-bar" style="top:295px">Medical Information</div>
  <div class="field-row" style="top:322px">Sex:<span class="fill fill--fixed" style="width:50px"></span>Height:<span class="fill fill--fixed" style="width:64px"></span>Weight:<span class="fill fill--fixed" style="width:60px"></span>Race:<span class="fill"></span></div>
  <div class="field-row" style="top:343px">Diagnosis:<span class="fill"></span></div>
  <div class="check-row" style="top:363px">
    <span><span class="box"></span>PCI (no. of stents:<span class="box-dots" style="width:26px"></span>)</span>
    <span><span class="box"></span>CABG (no. of vessels:<span class="box-dots" style="width:26px"></span>)</span>
    <span><span class="box"></span>MI (last event:<span class="box-dots" style="width:34px"></span>)</span>
    <span><span class="box"></span>PCM/ICD</span>
  </div>
  <div class="check-row" style="top:383px">
    <span><span class="box"></span>Diabetes</span>
    <span><span class="box"></span>Claustrophobia</span>
    <span><span class="box"></span>Asthma</span>
    <span><span class="box"></span>Emphysema</span>
    <span><span class="box"></span>COPD</span>
  </div>
  <div class="check-row" style="top:404px">
    <span>LMP:<span class="box-dots" style="width:62px"></span></span>
    <span><span class="box"></span>bHCG</span>
    <span><span class="box"></span>Tubal ligation</span>
    <span><span class="box"></span>Post-menopause &gt; 1 year</span>
    <span><span class="box"></span>Hysterectomy</span>
  </div>

  <p class="notice">Please read the following instructions carefully. You might be rescheduled if any of the following instructions are not met.</p>
  <ul class="instructions">
    <li>AVOID <b>caffeine</b> containing products (coffee, tea, soda, chocolate, energy drinks, or some over the counter medications) for 4 hours prior to testing.</li>
    <li>AVOID <b>smoking</b> for 4 hours prior to testing.</li>
    <li>AVOID <b>eating</b> or <b>drinking</b> anything except water for 4 hours prior to testing.</li>
    <li>Arrive <u>15 minutes</u> early for your appointment time.</li>
    <li>Wear comfortable clothing. <u>Remove any metal objects</u>, such as jewelry or piercings. Women will be asked to remove bras containing metal underwire.</li>
    <li>Inform your physician or the staff if you are claustrophobic or have a problem staying in restricted environments for any length of time.</li>
    <li>Inform the physician or the staff if you are or think you might be pregnant.</li>
  </ul>
  <p class="acknowledge">I hereby acknowledge that the instructions and procedures pertinent to this study were explained thoroughly, I had time to ask questions, and these questions were addressed satisfactorily.</p>

  <div class="sign-line" style="left:27px;top:594px">Patient's print name</div>
  <div class="sign-line" style="left:178px;top:594px">Patient's signature</div>
  <div class="sign-line" style="left:27px;top:635px">Prescriber's print name</div>
  <div class="sign-line" style="left:178px;top:635px">Prescriber's signature</div>

  <div class="referrer">
    <h4>Referring physician contact information</h4>
    <div>Order date:</div>
    <div>Tel no:</div>
    <div>Fax no:</div>
  </div>

  <p class="form-footer">Crestline Cardio, PLLC. Visit us at 218 Juniper Ave., Ste. B, Webster, TX 77412.<br>For appointments or more information on testing, please call (713) 642 1187, or visit crestlinecardio.example.</p>
</section>

</body>
</html>
```